Cover Design

This design is for a workbook that I use with my students. I am looking to refresh the cover design of the book. Attached is what the book cover looks like now and I don't like it. I'd really like to see something more creative, more modern and more inviting.

Need extra days to review

```html
<!DOCTYPE html>
<html lang="en">
<head>
<meta charset="utf-8">
<title>Talent Prep – HR Certification Workbook Cover</title>
<link href="https://fonts.googleapis.com/css2?family=Roboto:wght@900&family=Roboto+Condensed:wght@300;700&display=swap" rel="stylesheet">
<style>
  :root {
    --stage: #d9d9d7;
    --cover-white: #f4f4f4;
    --texture-light: #ececec;
    --texture-mid: #e2e2e2;
    --brand-red: #e0242c;
    --ink: #262626;
    --white: #ffffff;
  }
  * { margin: 0; padding: 0; box-sizing: border-box; }
  html, body {
    width: 1200px;
    height: 864px;
    overflow: hidden;
    background: var(--stage);
  }
  .canvas {
    position: relative;
    width: 1200px;
    height: 864px;
    display: flex;
    align-items: center;
    justify-content: center;
  }
  .book-cover {
    position: relative;
    width: 620px;
    height: 804px;
    background: var(--cover-white);
    box-shadow: 0 18px 40px rgba(0,0,0,0.18);
    overflow: hidden;
    display: flex;
    flex-direction: column;
  }
  .edition-band {
    height: 88px;
    background: var(--brand-red);
    display: flex;
    align-items: flex-end;
    padding: 0 0 20px 60px;
    flex-shrink: 0;
  }
  .edition-label {
    font-family: "Roboto Condensed", sans-serif;
    font-weight: 700;
    font-size: 22px;
    letter-spacing: 0.04em;
    color: var(--white);
    white-space: nowrap;
  }
  .cover-body {
    position: relative;
    flex: 1;
    padding: 40px 40px 0;
    display: flex;
    flex-direction: column;
    align-items: center;
  }
  .word-texture {
    position: absolute;
    inset: 0;
    background: linear-gradient(135deg, var(--texture-light) 0%, var(--cover-white) 45%, var(--texture-mid) 100%);
  }
  .cover-body > *:not(.word-texture) { position: relative; }
  .rule {
    width: 100%;
    height: 5px;
    background: var(--brand-red);
  }
  .title-block {
    display: flex;
    flex-direction: column;
    align-items: center;
    padding: 16px 0 18px;
    color: var(--ink);
    white-space: nowrap;
  }
  .title-main {
    font-family: "Roboto", sans-serif;
    font-weight: 900;
    font-size: 72px;
    line-height: 1;
    letter-spacing: 0.01em;
  }
  .title-sub {
    font-family: "Roboto Condensed", sans-serif;
    font-weight: 300;
    font-size: 62px;
    line-height: 1.08;
  }
  .title-workbook {
    font-family: "Roboto", sans-serif;
    font-weight: 900;
    font-size: 96px;
    line-height: 0.95;
  }
  .tagline {
    margin-top: 30px;
    text-align: center;
    font-family: "Roboto Condensed", sans-serif;
    font-weight: 700;
    color: var(--ink);
    line-height: 1.04;
    white-space: nowrap;
  }
  .tagline span { display: block; }
  .tagline .t1 { font-size: 28px; letter-spacing: 0.03em; }
  .tagline .t2 { font-size: 46px; }
  .tagline .t3 { font-size: 34px; }
  .tagline .t4 { font-size: 48px; }
  .author {
    margin-top: auto;
    margin-bottom: 44px;
    font-family: "Roboto Condensed", sans-serif;
    font-weight: 700;
    font-size: 60px;
    color: var(--brand-red);
    white-space: nowrap;
  }
</style>
</head>
<body>
<main class="canvas">
  <article class="book-cover">
    <header class="edition-band">
      <p class="edition-label">REVISED, UPDATED AND EXPANDED</p>
    </header>
    <section class="cover-body">
      <div class="word-texture" role="img" aria-label="Faint grey typographic cloud of HR terms such as opportunity, compliance, management, business, organization and workplace"></div>
      <div class="rule"></div>
      <h1 class="title-block">
        <span class="title-main">TALENT PREP</span>
        <span class="title-sub">HR CERTIFICATION</span>
        <span class="title-workbook">WORKBOOK</span>
      </h1>
      <div class="rule"></div>
      <p class="tagline">
        <span class="t1">EQUIPPING HR PROS</span>
        <span class="t2">WITH THE TOOLS NEEDED</span>
        <span class="t3">TO ACE THEIR</span>
        <span class="t4">CERTIFICATION EXAMS</span>
      </p>
      <p class="author">DANA WHITFIELD</p>
    </section>
  </article>
</main>
</body>
</html>
```